SEO AND WEB DESIGN COMPANY BUSINESS CARD DESIGN

I need an eye catching , simple business card design that will match my logo . I need 2 versions of it ( white background and black background) - SOME PEOPLE DID NOT GET IT AND SENDING US FRONT WHITE BACK WHITE VERSIONS WHICH IS NOT CORRECT.

ONE VERSION SHOULD BE BACK AND FRONT ALL BLACK , SECOND VERSION SHOULD BE BACK AND FRONT ALL WHITE

logo psd files are attached for both versions. The business card is going to have : First Name- Last name - position - phone numbers

```html
<!DOCTYPE html>
<html lang="en">
<head>
<meta charset="utf-8">
<title>Northlight Studio – Business Card, Black Version</title>
<link rel="stylesheet" href="https://fonts.googleapis.com/css2?family=Saira+Condensed:wght@500;600&family=Open+Sans:wght@400&display=swap">
<style>
  :root {
    --stage: #1b1b1c;
    --card: #0f0f10;
    --card-edge: #161617;
    --white: #f4f4f4;
    --blue: #5b8fd4;
    --rule: #6a6a6a;
  }
  * { box-sizing: border-box; margin: 0; padding: 0; }
  html, body {
    width: 1200px;
    height: 1200px;
    overflow: hidden;
    background: var(--stage);
  }
  .sheet {
    position: relative;
    width: 1200px;
    height: 1200px;
  }
  .card {
    position: absolute;
    left: 150px;
    width: 900px;
    height: 514px;
    border-radius: 28px;
    background: linear-gradient(160deg, var(--card-edge) 0%, var(--card) 60%);
    box-shadow: 0 20px 40px rgba(0,0,0,0.55);
    overflow: hidden;
  }
  .card--front { top: 56px; }
  .card--back { top: 630px; }

  .brand {
    font-family: "Saira Condensed", sans-serif;
    font-weight: 600;
    color: var(--white);
    letter-spacing: 1px;
    line-height: 1;
    white-space: nowrap;
  }
  .card--front .brand {
    position: absolute;
    left: 0;
    right: 0;
    top: 208px;
    text-align: center;
    font-size: 92px;
  }
  .card--back .brand {
    position: absolute;
    left: 40px;
    width: 400px;
    top: 228px;
    text-align: right;
    font-size: 50px;
  }
  .divider {
    position: absolute;
    left: 470px;
    top: 170px;
    width: 2px;
    height: 170px;
    background: var(--rule);
  }
  .contact {
    position: absolute;
    left: 505px;
    top: 178px;
  }
  .contact__name {
    font-family: "Saira Condensed", sans-serif;
    font-weight: 600;
    font-size: 54px;
    line-height: 1;
    color: var(--white);
  }
  .contact__role {
    font-family: "Saira Condensed", sans-serif;
    font-weight: 500;
    font-size: 26px;
    letter-spacing: 5px;
    color: var(--blue);
    margin-top: 4px;
  }
  .contact__list {
    list-style: none;
    margin-top: 18px;
    font-family: "Open Sans", sans-serif;
    font-size: 21px;
    color: var(--white);
  }
  .contact__item {
    display: flex;
    align-items: center;
    gap: 14px;
    margin-bottom: 6px;
  }
  .contact__icon { width: 22px; height: 22px; fill: var(--blue); flex: none; }
</style>
</head>
<body>
<main class="sheet">
  <section class="card card--front" aria-label="Card front">
    <p class="brand">NORTHLIGHT STUDIO</p>
  </section>

  <section class="card card--back" aria-label="Card back">
    <p class="brand">NORTHLIGHT STUDIO</p>
    <div class="divider"></div>
    <div class="contact">
      <h1 class="contact__name">DANIEL REYES</h1>
      <p class="contact__role">MANAGING DIRECTOR</p>
      <ul class="contact__list">
        <li class="contact__item">
          <svg class="contact__icon" viewBox="0 0 24 24" aria-hidden="true"><path d="M6.6 10.8a15.2 15.2 0 0 0 6.6 6.6l2.2-2.2a1 1 0 0 1 1-.25 11.4 11.4 0 0 0 3.6.57 1 1 0 0 1 1 1V20a1 1 0 0 1-1 1A17 17 0 0 1 3 4a1 1 0 0 1 1-1h3.5a1 1 0 0 1 1 1c0 1.25.2 2.45.57 3.6a1 1 0 0 1-.25 1z"/></svg>
          <span>555-0142-7730</span>
        </li>
        <li class="contact__item">
          <svg class="contact__icon" viewBox="0 0 24 24" aria-hidden="true"><path d="M2 5h20v14H2z M3.5 6.5 12 13l8.5-6.5" fill="none" stroke="#5b8fd4" stroke-width="1.8"/></svg>
          <span>daniel@northlight.example</span>
        </li>
      </ul>
    </div>
  </section>
</main>
</body>
</html>
```